[Fun Project] Design A Website For A Semi Pro Soccer Team!

DESIGN ONLY! [NO CODING NEEDED]

Hey,

Thanks for looking! Are you ready to design a cool project with us?

This may be a once in a lifetime opportunity to design a website for a Semi Pro Soccer Team. Projects like this don't come along very often! This will be a lot of fun for you!

We need a fresh and exciting website design for a new soccer (or football, depending on where you are) team. You can view the existing site here: http://www.pwxdunefc.com/

You can get a sense of the team colors and whatnot from that, but the layout is a little dull. We need something more like this: http://www.mendelhollow.com.

We need something that is visual and exciting, something that will appeal to a sports fan. Ideally, we'd love to work with a designer is a fan of the game, as we think he/she would design something more appealing to the demographic.

Be sure to follow the link below and check out our video:

http://clipnest.com/user4417032/review/30582714/4c1d7a90fe

Thank you and good luck!

Target Market(s)

Soccer/football fans and those interested in becoming fans. More than likely, we're talking males 18-40, but don't want to rule out females.

Font styles to use
Sans Serif

Colors
faee3e
fbed22
eb1f27
000000
f6f6f6

Requirements
Must have
• Picture/video slider in the top left (see video)
1 home page design and 2 interior page designs
Should not have
• Cluttered
Dull
Lame
Poor Design
And for the love of all the is holy please do not submit us a theme or a template from some website. We are smarter then that and will just remove you from the project....REAL Designers, we got your back and won't even consider crappy stuff....

```html
<!DOCTYPE html>
<html lang="en">
<head>
<meta charset="utf-8">
<title>Pewter Dune FC – Home</title>
<link rel="stylesheet" href="https://fonts.googleapis.com/css2?family=Open+Sans:ital,wght@0,400;0,600;0,700;1,800&family=Alfa+Slab+One&display=swap">
<style>
:root{
  --yellow:#fbed22;
  --gold:#f0cf2e;
  --red:#eb1f27;
  --deep-red:#a8141a;
  --black:#000000;
  --light:#f6f6f6;
  --white:#ffffff;
  --text:#333333;
  --muted:#555555;
}
*{margin:0;padding:0;box-sizing:border-box}
html,body{width:857px;height:1200px;overflow:hidden}
body{position:relative;font-family:"Open Sans",sans-serif;color:var(--text);
  background:linear-gradient(180deg,#141414 0px,#2a2a2a 180px,#4a3a2a 290px,#2f6b22 360px,#3f8f2a 450px,#2f7020 560px,#0e1a0c 640px,var(--black) 700px,var(--black) 1200px)}
.abs{position:absolute}
.side-glow{top:150px;width:110px;height:300px;
  background:radial-gradient(ellipse at center,rgba(210,170,70,.35),rgba(60,40,20,.25) 45%,transparent 72%)}
.side-glow.left{left:20px}
.side-glow.right{left:727px}
.top-ball{width:36px;height:36px;border-radius:50%;top:70px;background:radial-gradient(circle at 40% 35%,#fff,#bbb 70%,#555)}
/* nav */
.nav{left:123px;top:106px;width:611px;height:37px;background:var(--red);display:flex;font-size:9.5px;font-weight:600;color:var(--white)}
.nav a{color:inherit;text-decoration:none;display:flex;align-items:center;justify-content:center;border-right:1px solid #c4161d}
.nav a.active{background:var(--yellow);color:var(--black)}
.brand{left:387px;top:16px;width:99px;height:144px;display:flex;flex-direction:column;align-items:center;justify-content:center}
.brand .mark{width:72px;height:72px;border-radius:50%;background:var(--red);border:4px solid var(--yellow)}
.brand .name{margin-top:6px;font-size:10px;font-weight:700;color:var(--yellow);text-align:center;line-height:1.1}
/* slider */
.slider{left:123px;top:146px;width:611px;height:286px;background:var(--white);padding:5px}
.slide{position:relative;width:100%;height:100%;overflow:hidden;
  background:radial-gradient(ellipse at 60% 40%,#5a1a10,#1a0a06 70%,#000)}
.slide .photo{position:absolute;left:10px;top:35px;width:240px;height:225px;border-radius:40%;
  background:radial-gradient(ellipse,#d99a3a,#6a3a14 60%,transparent 72%)}
.slide .band{position:absolute;left:0;top:176px;width:600px;height:43px;background:var(--red)}
.slide .strip{position:absolute;left:2px;top:219px;width:598px;height:13px;background:var(--gold)}
.slide h1{position:absolute;left:235px;top:110px;font-family:"Alfa Slab One",serif;font-weight:400;font-size:23px;line-height:1.15;color:var(--white)}
.slide .tag{position:absolute;left:222px;top:180px;font-style:italic;font-weight:800;font-size:27px;letter-spacing:1px;color:var(--gold)}
.dots{position:absolute;left:21px;top:254px;display:flex;gap:4px}
.dots span{width:9px;height:9px;border-radius:50%;border:2px solid var(--white)}
.dots span.on{background:var(--red)}
/* results */
.result{top:449px;width:230px;height:103px;border:2px solid var(--white);color:var(--white);
  background:linear-gradient(180deg,#1f3a22,#2f6a26 45%,#4e9a2e)}
.result .crest{position:absolute;top:12px;width:40px;height:40px;border-radius:50%}
.result .crest.home{left:31px;background:#2b6cb5;border:3px solid var(--white)}
.result .crest.away{left:155px;background:var(--red);border:3px solid var(--white)}
.result .score{position:absolute;left:0;width:100%;top:14px;text-align:center;font-size:21px;font-weight:700}
.result .date{position:absolute;left:0;width:100%;top:43px;text-align:center;font-size:10px}
.result .team{position:absolute;top:60px;font-size:8.5px}
.result .btn{position:absolute;left:82px;top:69px;width:68px;height:24px;background:var(--yellow);color:var(--black);font-size:13px;font-weight:600;display:flex;align-items:center;justify-content:center}
.big-ball{left:390px;top:460px;width:90px;height:96px;border-radius:50%;background:radial-gradient(circle at 40% 35%,#fff,#ccc 65%,#444)}
/* content */
.panel{left:123px;top:570px;width:611px;height:540px;background:var(--white)}
.h2{font-size:15px;font-weight:400;color:#222}
.h2 em{font-style:normal;color:var(--red)}
.rule{height:1px;background:#ddd}
.welcome p.body{font-size:7.2px;line-height:13.6px;color:var(--muted);text-align:justify}
.btn-yellow{background:var(--gold);color:var(--white);font-size:8.5px;display:flex;align-items:center;justify-content:center}
.thumb{border:2px solid #eee}
.news-title{font-size:11px;color:#222}
.meta{font-size:7.5px;color:#444}
.excerpt{font-size:7.2px;line-height:13.5px;color:#444;text-align:justify}
.event{left:147px;width:275px;height:78px;background:var(--light);border:1px solid #e6e6e6}
.event .img{position:absolute;left:0;top:0;width:89px;height:78px}
.event .day{position:absolute;left:89px;top:0;width:30px;height:38px;background:var(--gold);color:var(--white);font-size:8px;display:flex;align-items:center;justify-content:center}
.event .mon{position:absolute;left:89px;top:38px;width:30px;height:40px;background:var(--black);color:var(--white);font-size:10px;display:flex;align-items:center;justify-content:center}
.event .t{position:absolute;left:135px;top:10px;font-size:8.5px;color:#222}
.event .p{position:absolute;left:135px;top:29px;font-size:7px;color:#444}
.event .d{position:absolute;left:135px;top:46px;width:135px;font-size:7px;line-height:12px;color:#444}
.radio{left:441px;top:877px;width:269px;height:205px;border:1px solid #e0e0e0;
  background:repeating-linear-gradient(45deg,#d6d6d6 0 1px,#e4e4e4 1px 3px)}
.radio h3{position:absolute;left:0;width:100%;top:15px;text-align:center;font-size:14px;font-weight:600;color:var(--deep-red)}
.radio .station{position:absolute;left:20px;top:46px;width:229px;height:107px;background:var(--gold);border:2px solid var(--white);display:flex;align-items:center;justify-content:center;gap:8px}
.radio .station i{width:14px;height:14px;background:var(--red)}
.radio .station b{font-size:16px;font-weight:700;color:var(--red)}
.radio p{position:absolute;left:20px;top:171px;width:230px;font-size:10.5px;line-height:13px;color:#222}
/* footer */
.foot-links{left:123px;top:1139px;font-size:7.5px;color:#ddd;word-spacing:1px}
.copy{left:123px;top:1161px;font-size:7.5px;color:#ddd}
.social{top:1145px;width:23px;height:23px;border-radius:50%;background:radial-gradient(circle at 40% 35%,#666,#2a2a2a)}
</style>
</head>
<body>
<div class="abs side-glow left" role="img" aria-label="Celebrating player photo area, left edge"></div>
<div class="abs side-glow right" role="img" aria-label="Celebrating player photo area, right edge"></div>
<div class="abs top-ball" style="left:227px" role="img" aria-label="Soccer ball"></div>
<div class="abs top-ball" style="left:590px" role="img" aria-label="Soccer ball"></div>

<nav class="abs nav">
  <a class="active" style="width:71px">Home</a>
  <a style="width:73px">News</a>
  <a style="width:65px">Stats</a>
  <a style="width:65px">About</a>
  <a style="width:93px;border-right:none"></a>
  <a style="width:58px">Tickets</a>
  <a style="width:69px">Team Shop</a>
  <a style="width:69px">The FDL</a>
  <a style="width:48px;border-right:none">Log In</a>
</nav>
<div class="abs brand"><div class="mark"></div><div class="name">Pewter Dune</div></div>

<section class="abs slider">
  <div class="slide">
    <div class="photo" role="img" aria-label="Player striking a ball in mid-air"></div>
    <div class="band"></div><div class="strip"></div>
    <h1>Pewter Dune<br>Football Club</h1>
    <div class="tag">Kicks Off This Spring!</div>
    <div class="dots"><span class="on"></span><span></span><span></span><span></span></div>
  </div>
</section>

<div class="abs result" style="left:123px">
  <div class="crest home"></div><div class="crest away"></div>
  <div class="score">3 - 1</div><div class="date">16 Feb 2014</div>
  <div class="team" style="left:32px">Harbor City</div><div class="team" style="left:158px">Redstone</div>
  <div class="btn">Tickets</div>
</div>
<div class="abs big-ball" role="img" aria-label="Soccer ball"></div>
<div class="abs result" style="left:504px">
  <div class="crest home"></div><div class="crest away"></div>
  <div class="score">3 - 1</div><div class="date">16 Feb 2014</div>
  <div class="team" style="left:32px">Harbor City</div><div class="team" style="left:158px">Redstone</div>
  <div class="btn">Tickets</div>
</div>

<main class="abs panel"></main>

<section class="welcome">
  <svg class="abs" style="left:146px;top:590px" width="20" height="31" viewBox="0 0 20 31"><rect x="6" y="0" width="8" height="17" rx="4" fill="#111"/><path d="M2 12 v2 a8 8 0 0 0 16 0 v-2" stroke="#111" stroke-width="2" fill="none"/><rect x="9" y="22" width="2" height="6" fill="#111"/><rect x="4" y="28" width="12" height="2" fill="#111"/></svg>
  <h2 class="abs h2" style="left:173px;top:590px">Welcome To <em>Pewter Dune</em></h2>
  <div class="abs" style="left:173px;top:613px;font-size:9px;color:#222">OFFICIAL SITE OF THE</div>
  <p class="abs body" style="left:147px;top:638px;width:269px">FDL Soccer is coming to Pewter Dune! The FDL is the top developmental men's league in North America. The 2013 FDL featured 64 teams within four conferences throughout the United States and Canada. The FDL season consists of 14 regular season matches for each team, seven home and seven away, and provides elite collegiate players the opportunity to taste a higher level of competition while maintaining their eligibility. In addition to league play, FDL teams compete in the Meridian Open Cup as well as various exhibitions. The FDL has proven to be an important stepping-stone for top professionals now playing throughout the world.</p>
  <div class="abs" style="left:149px;top:768px;font-size:8.5px;font-weight:600;color:#111">Download and Print the 2014 Pewter Dune Full Schedule!</div>
  <div class="abs btn-yellow" style="left:148px;top:808px;width:61px;height:26px">Read More</div>
</section>

<section>
  <h2 class="abs h2" style="left:441px;top:586px">News &amp; Event</h2>
  <div class="abs rule" style="left:441px;top:618px;width:269px"></div>
  <div class="abs thumb" style="left:441px;top:640px;width:100px;height:79px;background:linear-gradient(160deg,#5a3a30,#b52a20 70%,#d8c030)" role="img" aria-label="Morning show interview video still"></div>
  <div class="abs news-title" style="left:559px;top:635px">Interview with the Morning</div>
  <div class="abs meta" style="left:559px;top:663px">Owen T. Hale</div>
  <p class="abs excerpt" style="left:559px;top:682px;width:151px">Merynasas setyera krsca vertyunade ertyao lasec vasptai aoertayse squrem ipsum quia dolor. Vsanamet, consect</p>
  <div class="abs rule" style="left:441px;top:736px;width:269px"></div>
  <div class="abs thumb" style="left:441px;top:756px;width:100px;height:79px;background:linear-gradient(160deg,#3a4a5a,#6a5a50 60%,#2a2a2a)" role="img" aria-label="First fan video still"></div>
  <div class="abs news-title" style="left:559px;top:751px">First Fan</div>
  <div class="abs meta" style="left:559px;top:779px">Owen T. Hale</div>
  <p class="abs excerpt" style="left:559px;top:798px;width:151px">Merynasas setyera krsca vertyunade ertyao lasec vasptai aoertayse squrem ipsum quia dolor. Vsanamet, consect</p>
</section>

<section>
  <h2 class="abs h2" style="left:147px;top:872px">UpComing <em style="color:var(--deep-red)">Events</em></h2>
  <div class="abs rule" style="left:147px;top:900px;width:275px"></div>
  <article class="abs event" style="top:914px">
    <div class="img" role="img" aria-label="Match action photo" style="background:linear-gradient(135deg,#6a7a8a,#c8d0d8 50%,#3a6a2a)"></div>
    <div class="day">10</div><div class="mon">Jan</div>
    <div class="t">DUST IN THE WIND</div><div class="p">Posted by: Tessly</div>
    <div class="d">Morbi tempor quam vel massa adpi congue pelle ntesque niselel com.</div>
  </article>
  <article class="abs event" style="top:1006px">
    <div class="img" role="img" aria-label="Player on the ball photo" style="background:linear-gradient(135deg,#d8a030,#3a4aa0 50%,#3a8a2a)"></div>
    <div class="day">10</div><div class="mon">Jan</div>
    <div class="t">DUST IN THE WIND</div><div class="p">Posted by: Tessly</div>
    <div class="d">Morbi tempor quam vel massa adpi congue pelle ntesque niselel com.</div>
  </article>
</section>

<aside class="abs radio">
  <h3>Check Us Out on the Radio!</h3>
  <div class="station"><i></i><b>Sportline 104.3</b></div>
  <p>Team President Dev Marlow sits down with 104.3 Sportline Radio!</p>
</aside>

<footer>
  <div class="abs foot-links">HOME &nbsp;| &nbsp;ABOUT &nbsp;| &nbsp;NEWS | VIDEOS | TICKETS | CONTACT</div>
  <div class="abs copy">Copyright © 2014 Pewter Dune.All rights reserved.</div>
  <span class="abs social" style="left:624px" aria-label="Social link"></span>
  <span class="abs social" style="left:652px" aria-label="Social link"></span>
  <span class="abs social" style="left:681px" aria-label="Social link"></span>
  <span class="abs social" style="left:709px" aria-label="Social link"></span>
</footer>
</body>
</html>
```